Community Legal Website

The website is about a law in legal area (Fiscal), it has a moderator and the community also contributes with information.

Attention that this is not for a Law Firm. This is a community site where all the lawyers can contribute wiith their knowledge and at the same time where they can read the Official Law in the fiscal area.

The site is in portuguese, but we have attach information in english about the functionalities.

I attach information which represents the first version of the site done by html.. That is the site we intend to improve.

The site is quite simple because the main pages are:
- Home page;
- Section page (which has the Chapters and articles)
- Article page;

This pages all belong to the article:

redaccao_actual.htm, redaccoes_anteriores.htm, anotacoes.htm, jurisprudencia.htm, decisoesadministrativas.htm, minutas.htm, duvidas.htm

AS you see in all of them the options are always there.

The most important in this site is the usability of the content:

The FAQ, Contacts, Terms of conditions, who we are, are links less important.

Also there is a possibility to have in the homepage a higligh of certain articles that we want to raise from the others.

Please check the excel sheet as well as the zip file wich has the site in portuguese that you can use a website translator to check in your language.
Updates

We added a excel sheet with the functionalities in english which the site must have.

Reason: Because this is easter time we have increased the time for the deliver

Please check briefing update.

Reason: There were some request to extend the deadline because of the Easter

Hi!

Please read carefully the briefing. People are presenting me company web sites adn this is NOT a company web site. THis is a Site wich has a content of Laws. Please check the 1st version in the zip file and improve it. The options are there and you can translate in google tradutor or reading the excel sheet attach.

txs,
JV

Reason: My client need more desing choices

Target Market(s)

Lawyers, jurists and people related with the fiscal Law.

Industry/Entity Type

Legal

Requirements
Must have
• The interface should be clean and elegant.
It should also contribute to speed.
And try to avoid to many distract elements.
The site will be dinamic and with a backoffice, so in that you have to be carefully with the space dynamic. But you don't have to worry about the backoffice. Only the front office which is the public site.

```html
<!DOCTYPE html>
<html lang="pt">
<head>
<meta charset="utf-8">
<title>LEXFISCO.net — Legislação Fiscal</title>
<link rel="stylesheet" href="https://fonts.googleapis.com/css2?family=Raleway:wght@300;400;500&display=swap">
<style>
  :root {
    --page-bg: #ffffff;
    --teal-dark: #4e6a69;
    --teal-light: #8fb0ae;
    --teal-pale: #c9dad9;
    --ink: #3f4a4a;
    --muted: #8c9393;
    --rule: #d7dcdc;
    --footer-bg: #dcdfdf;
    --footer-ink: #7b8282;
  }
  * { box-sizing: border-box; margin: 0; padding: 0; }
  html, body {
    width: 1200px; height: 776px; overflow: hidden;
    background: var(--page-bg);
    font-family: "Raleway", sans-serif;
    color: var(--ink);
  }
  .site {
    position: relative; width: 1200px; height: 776px;
  }

  /* Header */
  .site-header {
    position: absolute; left: 0; top: 0; width: 1200px; height: 150px;
  }
  .brand {
    position: absolute; left: 70px; top: 40px;
    display: flex; align-items: center; gap: 14px;
  }
  .brand-dot {
    width: 18px; height: 18px; border-radius: 50%;
    background: var(--teal-dark);
  }
  .brand-name {
    font-weight: 300; font-size: 34px; letter-spacing: 3px;
    color: var(--teal-dark);
  }
  .utility-links {
    position: absolute; right: 60px; top: 34px;
    display: flex; gap: 22px; list-style: none;
    font-size: 12px; color: var(--muted); letter-spacing: 0.5px;
  }
  .main-nav {
    position: absolute; left: 0; top: 110px; width: 1200px; height: 30px;
    background: var(--teal-light);
    display: flex; justify-content: flex-end; align-items: center;
    padding-right: 60px; gap: 30px; list-style: none;
    font-size: 12px; color: #fff; letter-spacing: 1px; text-transform: uppercase;
  }

  /* Content */
  .content {
    position: absolute; left: 60px; top: 180px; width: 1080px;
  }
  .illustration-scales {
    position: absolute; left: 0; top: 6px; width: 150px; height: 120px;
    background: linear-gradient(160deg, #eef1f1, #d5dbdb);
  }
  .law-section {
    position: absolute; left: 0; width: 1080px;
  }
  .law-section.irs { top: 0; }
  .law-section.administrative { top: 260px; }

  .article-list {
    list-style: none; margin-left: 190px;
    font-size: 13px; color: var(--muted); letter-spacing: 0.3px;
  }
  .article-list li {
    padding: 7px 0; border-bottom: 1px solid var(--rule);
  }
  .section-band {
    margin-top: 16px; height: 40px;
    background: var(--teal-dark); color: #fff;
    display: flex; justify-content: flex-end; align-items: center;
    padding-right: 24px;
    font-weight: 300; font-size: 22px; letter-spacing: 2px; text-transform: uppercase;
  }
  .section-band.first { margin-left: 190px; }
  .administrative .section-band { margin-top: 0; margin-bottom: 14px; }
  .administrative .article-list { margin-left: 0; }

  .section-rule {
    position: absolute; left: 60px; top: 640px; width: 1080px; height: 1px;
    background: var(--rule);
  }

  /* Footer */
  .site-footer {
    position: absolute; left: 0; bottom: 0; width: 1200px; height: 70px;
    background: var(--footer-bg);
    display: flex; justify-content: flex-end; align-items: center;
    padding-right: 60px; gap: 18px;
    font-size: 12px; color: var(--footer-ink);
  }
  .footer-icons { display: flex; gap: 8px; }
  .footer-icons span {
    width: 16px; height: 16px; border-radius: 50%;
    background: #9aa2a2;
  }
</style>
</head>
<body>
<div class="site">
  <header class="site-header">
    <div class="brand">
      <span class="brand-dot"></span>
      <span class="brand-name">LEXFISCO.net</span>
    </div>
    <ul class="utility-links">
      <li>Quem somos</li>
      <li>Contactos</li>
      <li>Termos</li>
    </ul>
    <ul class="main-nav">
      <li>Início</li>
      <li>Legislação</li>
      <li>Dúvidas</li>
    </ul>
  </header>

  <main class="content">
    <div class="illustration-scales" role="img" aria-label="Ilustração de uma balança da justiça"></div>

    <section class="law-section irs">
      <ul class="article-list">
        <li>Capítulo I – Incidência real e pessoal do imposto</li>
        <li>Capítulo II – Rendimentos isentos e dedução específica</li>
        <li>Capítulo III – Determinação do rendimento coletável</li>
      </ul>
      <h2 class="section-band first">Código do IRS</h2>
    </section>

    <section class="law-section administrative">
      <h2 class="section-band">Legislação Administrativa Anotada</h2>
      <ul class="article-list">
        <li>Capítulo I – Procedimento e processo tributário anotado</li>
      </ul>
    </section>
  </main>

  <div class="section-rule"></div>

  <footer class="site-footer">
    <span>Ajuda frequente</span>
    <div class="footer-icons"><span></span><span></span><span></span></div>
  </footer>
</div>
</body>
</html>
```